website design of a new wearable phone/gps called Brava Band

We are launching a product called Brava Band. Watch is a stand-alone cellular watch that allows anyone from kids to seniors to make phone calls by simply pushing one of four buttons on the watch. The SOS button connects you to a live team of emergency professionals that can patch you to a 911 operator. Two of the other buttons are programmable to dial any desired phone number. The fourth button (called the "Magic" button) connects you with a live team of personal assistants that can help you with anything you want, including transferring you to any number, making dinner reservations, answering trivia, finding movie times and anything else you can imagine. Our slogan is: "Always safe with Brava Band"
The built-in GPS functionality of the watch allows you to track the location of the watch at any time from the Brava Band website or the Brava Band app. You can also set up a perimeter around a specific area so that you can receive alerts when the watch travels outside of the "geofence".
There is a website that sells a similar product at http://www.quendo-kids.example - we like the look/feel and simplicity of this site. Now while we don't want a direct copy of this site, we would like a site that incorporates the simplicity of its layout and use of colors and images from the quendo-kids.example site.
We have included in the materials the Brava Band logo (in Adobe Illustrator).
We would like a site that shares the colors used for our logo. Please use stock images that you see fit to use for the mockup. We will be providing custom photographed images for the final site.
We would like to start first with the home page design, and when we select a winning designer, we would like for them to create the "About", "Technology", "Store" and "Support" pages.
For the home page, for now you can use the same content as they have on the quendo-kids.example site - ours will be different, but we are still working on creating the final copy that will go on the site.
We would like final deliverable code to be responsive (for mobile etc)
Any questions, let us know.

```html
<!DOCTYPE html>
<html lang="en">
<head>
<meta charset="utf-8">
<title>Brava Band</title>
<link href="https://fonts.googleapis.com/css2?family=Open+Sans:wght@400;600&display=swap" rel="stylesheet">
<style>
:root{
  --accent:#5fd3ee;
  --ink:#333333;
  --muted:#555555;
  --light-grey:#dcdcdc;
  --dark-grey:#6d6d6d;
  --icon-grey:#b5b5b5;
  --white:#ffffff;
}
*{box-sizing:border-box;margin:0;padding:0}
html,body{width:834px;height:1200px;overflow:hidden}
body{position:relative;font-family:"Open Sans",Arial,sans-serif;color:var(--ink);background:var(--white)}
.abs{position:absolute}
.brand{font-weight:600;color:var(--ink);white-space:nowrap}

/* header */
.site-header{left:0;top:0;width:834px;height:30px;background:var(--white)}
.site-header .brand{position:absolute;left:140px;top:7px;font-size:11px}
.main-nav{position:absolute;right:134px;top:9px;display:flex;gap:15px;font-size:7.5px}
.main-nav a{color:var(--ink);text-decoration:none}
.main-nav a.active{color:var(--accent)}

/* hero */
.hero{left:0;top:30px;width:834px;height:293px;
  background:linear-gradient(90deg,#c9cfd6 0%,#e4dde0 35%,#d6c1b8 62%,#c4a08c 82%,#d9cbc4 100%)}
.hero .brand{position:absolute;left:0;width:834px;text-align:center;top:200px;font-size:34px;line-height:40px}
.hero-tagline{position:absolute;left:0;width:834px;top:236px;text-align:center;color:var(--white);font-size:18px;letter-spacing:1px}

/* intro */
.intro-title{left:74px;top:403px;font-size:19px;font-weight:400;color:var(--accent)}
.intro-text{left:74px;top:431px;width:426px;font-size:7px;line-height:10px;color:var(--muted)}
.product-visual{left:580px;top:346px;width:180px;height:218px;
  background:linear-gradient(160deg,#f1f1f1 0%,#e6e2da 50%,#f6f6f6 100%)}

/* features */
.features{left:0;top:571px;width:834px;height:299px;background:var(--accent);color:var(--white)}
.feature{position:absolute;width:240px;text-align:center}
.feature-num{width:48px;height:48px;margin:0 auto;border:3px solid var(--white);border-radius:50%;
  font-size:32px;line-height:42px}
.feature-title{font-size:15.5px;margin-top:2px}
.feature-text{font-size:7px;line-height:10px;margin-top:4px}

/* follow */
.follow{left:0;top:903px;width:834px;text-align:center}
.follow h2{font-size:15.5px;font-weight:400}
.follow p{font-size:7px;color:var(--muted);margin-top:6px}
.social{display:flex;justify-content:center;gap:32px;margin-top:20px}
.social span{width:28px;height:28px;border-radius:4px;background:var(--icon-grey)}

/* footer */
.site-footer{left:0;top:1026px;width:834px;height:144px;background:var(--light-grey)}
.footer-col{position:absolute;top:29px}
.footer-col h3{font-size:9.5px;font-weight:400;color:var(--muted);margin-bottom:3px}
.footer-col li{list-style:none;font-size:7px;color:var(--muted);line-height:15px;padding-left:11px;position:relative}
.footer-col li::before{content:"";position:absolute;left:1px;top:5px;width:4px;height:4px;
  border-top:1px solid var(--muted);border-right:1px solid var(--muted);transform:rotate(45deg)}
.site-footer .brand{position:absolute;left:557px;top:30px;font-size:20px}
.copyright{left:0;top:1170px;width:834px;height:30px;background:var(--dark-grey);color:var(--white);
  font-size:7px;text-align:center;line-height:30px}
</style>
</head>
<body>

<header class="site-header abs">
  <div class="brand">Brava Band</div>
  <nav class="main-nav">
    <a class="active" href="#">Top</a><a href="#">About</a><a href="#">Technology</a><a href="#">Store</a><a href="#">Support</a>
  </nav>
</header>

<section class="hero abs" role="img" aria-label="Support operator with headset working at a computer in a call centre">
  <div class="brand">Brava Band</div>
  <p class="hero-tagline">Always safe with Brava Band</p>
</section>

<h2 class="intro-title abs">Tag line about Brava Band</h2>
<p class="intro-text abs">Brava Band is a stand-alone cellular watch that allows anyone from kids to seniors to make phone calls by simply pushing one of four buttons on the watch. Lorem ipsum dolor sit amet, consectetur adipiscing elit. Phasellus non mi tristique, pretium mi ut, ornare augue. Maecenas placerat feugiat eros non ullamcorper. Nunc ut elit eget ante volutpat hendrerit. Suspendisse ut nibh quis nisl aliquam euismod. Fusce accumsan dapibus pellentesque. Mauris dignissim, mauris eget dignissim viverra, enim magna porttitor neque, quis pellentesque erat ligula in elit.</p>
<div class="product-visual abs" role="img" aria-label="Product photo of the Brava Band smartwatch on a leather strap"></div>

<section class="features abs">
  <div class="feature" style="left:144px;top:33px">
    <div class="feature-num">1</div>
    <div class="feature-title">SOS</div>
    <p class="feature-text">Connects you to a live team of emergency professionals that can patch you to a 911 operator</p>
  </div>
  <div class="feature" style="left:450px;top:33px">
    <div class="feature-num">2</div>
    <div class="feature-title">Programmable</div>
    <p class="feature-text">Can be programmed to dial any desired phone number</p>
  </div>
  <div class="feature" style="left:144px;top:148px">
    <div class="feature-num">3</div>
    <div class="feature-title">Programmable</div>
    <p class="feature-text">Can be programmed to dial any desired phone number</p>
  </div>
  <div class="feature" style="left:450px;top:148px">
    <div class="feature-num">4</div>
    <div class="feature-title">Magic Button</div>
    <p class="feature-text">Connects you with a live team of personal assistants that can help you with anything you want, including transferring you to any number, making dinner reservations, answering trivia, finding movie times and anything else you can imagine</p>
  </div>
</section>

<section class="follow abs">
  <h2>Follow Us</h2>
  <p>Receive updates about Brava Band on your favourite social media</p>
  <div class="social" aria-label="Social media links"><span></span><span></span><span></span></div>
</section>

<footer class="site-footer abs">
  <div class="footer-col" style="left:163px"><h3>Menu</h3><ul><li>Top</li><li>About</li><li>Technology</li><li>Store</li><li>Support</li></ul></div>
  <div class="footer-col" style="left:294px"><h3>Support</h3><ul><li>FAQ</li><li>Troubleshooting</li><li>Contact</li><li>ToS</li></ul></div>
  <div class="footer-col" style="left:424px"><h3>Store</h3><ul><li>Store front</li><li>New in stock</li><li>Top sellers</li><li>Warranty</li></ul></div>
  <div class="brand">Brava Band</div>
</footer>
<div class="copyright abs">© 2016 Brava Band. All rights reserved.</div>

</body>
</html>
```